Webdesign für Coaching von Erwachsenen und Kindern
Zielgruppe
Ich coache Erwachsene und Kinder mit den Methoden des NLP. Meine Zielgruppe sind primär Eltern und auch Lehrer. Mein Ziel sind mehr glückliche Kinder, indem ich primär die Eltern und teilweise auch die Kinder coache.
Mir ist es wichtig souverän und nicht wie eine Kindergärtnerin zu wirken.
Aufgabenstellung
Meine Website: www.coach-merlinger.ch ist mit Wordpress erstellt.
Das Logo besteht bereits und soll so belassen werden. Die Farben des Logos dürfen aufgegriffen werden. Es soll alles zusammenpassen und 'rund' wirken.
Mir gefällt zum Beispiel die Website lumaquo.ch oder Pflegewerk-nord.ch

```html
<!DOCTYPE html>
<html lang="de">
<head>
<meta charset="utf-8">
<title>Sabine Merlinger – Coaching für glückliche Kinder</title>
<link rel="stylesheet" href="https://fonts.googleapis.com/css2?family=Kalam:wght@300;400;700&family=Montserrat:wght@400;500;600;700&display=swap">
<style>
:root{
  --navy:#1c3b86;
  --blue:#1f6fc0;
  --ink:#2d2f36;
  --muted:#8f96a6;
  --hero:#eef2f9;
  --band:#dde6f3;
  --blob:#e4ebf6;
  --paper:#fbfbfc;
  --star:#f0a23a;
  --quote:#d3dcec;
}
*{box-sizing:border-box;margin:0;padding:0}
html,body{width:1200px;height:4482px;overflow:hidden}
body{position:relative;background:var(--paper);font-family:'Montserrat',sans-serif;color:var(--ink);font-size:13.5px;line-height:1.55}
.abs{position:absolute}
.bg{position:absolute;left:0;top:0;width:1200px;height:4482px}
.script{font-family:'Kalam',cursive;font-weight:300;color:var(--navy)}
.script b{font-weight:700}
.nav a{font-size:13.5px;color:var(--ink);text-decoration:none;margin-right:36px}
.nav a.active{border-bottom:1px solid var(--ink)}
.brand{font-family:'Kalam',cursive;font-weight:400;font-size:34px;line-height:44px;color:var(--navy);white-space:nowrap;display:flex;align-items:center;justify-content:center;gap:10px}
.brand-dot{width:12px;height:12px;border-radius:50%;background:var(--blue)}
.mail-top{font-size:13.5px;display:flex;align-items:center;gap:8px;white-space:nowrap}
.btn{display:inline-block;background:var(--blue);color:#fff;border:2px solid var(--navy);border-radius:24px;font-size:13.5px;font-weight:500;text-transform:uppercase;text-align:center;line-height:40px;height:44px;text-decoration:none}
.hero-title{font-size:50px;line-height:58px}
.h2{font-size:44px;line-height:1.1}
.feature{width:250px;text-align:center}
.feature .ic{display:block;width:72px;height:72px;margin:0 auto 24px}
.feature h3{font-family:'Kalam',cursive;font-weight:300;font-size:22px;color:var(--ink);margin-bottom:16px}
.feature p{font-size:13.5px;line-height:21px}
.text p{margin-bottom:21px;line-height:21px}
.strong-blue{color:var(--navy);font-weight:600}
.card{background:#fff;border-radius:12px;padding:30px 28px;width:308px}
.card .q{font-family:'Kalam',cursive;font-size:110px;line-height:70px;height:54px;color:var(--quote);font-weight:700}
.card p{font-size:13.5px;line-height:21px;margin:10px 0 20px}
.who{display:flex;align-items:center;gap:16px}
.avatar{width:48px;height:48px;border-radius:50%;background:radial-gradient(circle at 50% 40%,#d9b59c,#7d6350)}
.who b{display:block;font-size:13px;font-weight:600}
.stars{color:var(--star);font-size:17px;letter-spacing:2px}
.arrow{width:52px;height:52px;border-radius:50%;background:var(--blue);border:2px solid var(--navy)}
.field{border:1px solid var(--blue);background:#fff;font-size:13px;color:var(--muted);padding:12px 14px}
.info{display:flex;align-items:center;gap:20px}
.info .ring{width:58px;height:58px;border-radius:50%;border:2px solid var(--blue);display:flex;align-items:center;justify-content:center}
.info b{display:block;font-size:13.5px;font-weight:600}
.footer a{font-size:13px;font-weight:500;color:var(--ink);text-decoration:none;margin:0 18px;text-transform:uppercase}
</style>
</head>
<body>

<svg class="bg" viewBox="0 0 1200 4482" aria-hidden="true">
  <rect x="0" y="0" width="1200" height="638" fill="var(--hero)"/>
  <path d="M0 638H1200V1140C1060 1110 950 1200 800 1222C650 1244 560 1165 420 1152C255 1138 120 1200 0 1262Z" fill="var(--band)"/>
  <path d="M0 1790C120 1770 170 1890 270 1950C370 2010 330 2160 190 2205C110 2232 50 2205 0 2235Z" fill="var(--blob)"/>
  <path d="M0 2905C150 2870 260 2945 420 2962C600 2982 700 2900 850 2952C960 2992 1020 3070 1200 3060V3845C1010 3880 900 3828 700 3840C500 3852 300 3812 0 3800Z" fill="var(--band)"/>
  <rect x="0" y="4406" width="1200" height="76" fill="var(--band)"/>
</svg>

<!-- Header -->
<nav class="nav abs" style="left:110px;top:86px">
  <a href="#">Angebote</a><a href="#" class="active">Über Mich</a><a href="#">Kontakt</a>
</nav>
<div class="brand abs" style="left:450px;top:74px;width:300px"><span class="brand-dot"></span>Sabine Merlinger</div>
<div class="mail-top abs" style="left:805px;top:86px">
  <svg width="14" height="11" viewBox="0 0 14 11"><rect x="0.7" y="0.7" width="12.6" height="9.6" rx="1" fill="none" stroke="var(--blue)" stroke-width="1.4"/><path d="M1 1.5L7 6L13 1.5" fill="none" stroke="var(--blue)" stroke-width="1.4"/></svg>
  sabine@coach-merlinger.ch
</div>

<!-- Hero -->
<h1 class="script hero-title abs" style="left:108px;top:228px"><b>Glückliche Kinder</b> durch<br>entspannte Eltern,<br>Lehrerinnen und Lehrer</h1>
<p class="abs" style="left:110px;top:422px;width:540px;line-height:21px">Ich coache Eltern, Lehrerinnen und Lehrer und Kinder im Einzelsetting und biete Workshops für mehrere Personen an.</p>
<a class="btn abs" style="left:110px;top:496px;width:220px" href="#">Zum Kontaktformular</a>
<div class="abs" role="img" aria-label="Foto: zwei lachende Kinder, Junge und Mädchen, auf die Arme gestützt" style="left:670px;top:200px;width:530px;height:438px;background:radial-gradient(ellipse at 55% 50%,#e9d6c8 0%,#e3e6ee 55%,var(--hero) 80%)"></div>

<!-- NLP -->
<h2 class="script h2 abs" style="left:0;top:718px;width:1200px;text-align:center">Neuro-Linguistisches <b>Proagrammieren</b></h2>
<p class="abs" style="left:330px;top:782px;width:540px;text-align:center;line-height:21px">Wollen Sie Leichtigkeit, eine einfache Kommunikation mit ihrem Kind und weniger Ängste? Mehr Vertrauen und Zuversicht und weniger Streit?</p>

<div class="feature abs" style="left:158px;top:874px">
  <svg class="ic" viewBox="0 0 72 72"><circle cx="36" cy="36" r="35" fill="none" stroke="var(--blue)" stroke-width="1.5"/><circle cx="36" cy="36" r="29" fill="none" stroke="var(--navy)" stroke-width="1"/><path d="M28 36.5L34 42L45 30" fill="none" stroke="var(--navy)" stroke-width="2" stroke-linecap="round" stroke-linejoin="round"/></svg>
  <h3>Vorteil 1</h3>
  <p>Lorem ipsum dolor sit amet, consectetur adipiscing elit, sed do eiusmod tempor incididunt ut Risus commodo viverra accumsan lacus vel facilisis.</p>
</div>
<div class="feature abs" style="left:475px;top:874px">
  <svg class="ic" viewBox="0 0 72 72"><circle cx="36" cy="36" r="35" fill="none" stroke="var(--blue)" stroke-width="1.5"/><circle cx="36" cy="36" r="29" fill="none" stroke="var(--navy)" stroke-width="1"/><path d="M28 36.5L34 42L45 30" fill="none" stroke="var(--navy)" stroke-width="2" stroke-linecap="round" stroke-linejoin="round"/></svg>
  <h3>Vorteil 2</h3>
  <p>Lorem ipsum dolor sit amet, consectetur adipiscing elit, sed do eiusmod tempor incididunt ut Risus commodo viverra accumsan lacus vel facilisis.</p>
</div>
<div class="feature abs" style="left:783px;top:874px">
  <svg class="ic" viewBox="0 0 72 72"><circle cx="36" cy="36" r="35" fill="none" stroke="var(--blue)" stroke-width="1.5"/><circle cx="36" cy="36" r="29" fill="none" stroke="var(--navy)" stroke-width="1"/><path d="M28 36.5L34 42L45 30" fill="none" stroke="var(--navy)" stroke-width="2" stroke-linecap="round" stroke-linejoin="round"/></svg>
  <h3>Vorteil 3</h3>
  <p style="font-weight:500">Lorem ipsum dolor sit amet, consectetur adipiscing elit, sed do eiusmod tempor incididunt ut Risus commodo viverra accumsan lacus vel facilisis.</p>
</div>

<!-- Über mich -->
<h2 class="script h2 abs" style="left:110px;top:1318px">Über <b>Mich</b></h2>
<div class="text abs" style="left:110px;top:1380px;width:440px">
  <p>In einer Grossfamilie aufgewachsen, habe ich schnell gelernt zu helfen und mich um meine kleineren Geschwister zu kümmern.</p>
  <p>Von zu Hause ausgezogen, widmete ich mich erstmals dem Studium der Tiermedizin und arbeitete als Tierärztin.</p>
  <p>Als ich später selbst Mama wurde, habe ich die Begeisterung für das Wohlergehen von Kindern wieder entdeckt und eine Ausbildung zum NLP-Coach gemacht. Diese hilft mir immer wieder auch im Umgang mit meinem eigenen Kind, in der Partnerschaft und in der Kommunikation mit allen anderen Menschen.</p>
  <p>Ich spüre, was mein Gegenüber braucht und was ihm helfen könnte, mache liebevolle Angebote unter Anwendung der Techniken des NLP.</p>
  <p>NLP begeistert mich immer wieder aufs Neue und ich freue mich über jedes Coaching und über jeden Menschen, dem ich weiterhelfen konnte.</p>
</div>
<div class="abs" role="img" aria-label="Porträtfoto der Coachin, lächelnd, dunkles Haar, dunkler Blazer" style="left:617px;top:1315px;width:583px;height:520px;background:linear-gradient(180deg,#dedede 0%,#cfc7c1 45%,#3a3a40 100%)"></div>

<!-- Angebot -->
<svg class="abs" style="left:182px;top:2000px" width="376" height="376" viewBox="0 0 376 376" role="img" aria-label="Runder Fotoausschnitt: lächelndes Mädchen mit langen blonden Haaren im gestreiften Shirt">
  <defs><radialGradient id="girl" cx="50%" cy="40%" r="60%"><stop offset="0" stop-color="#ecd9c6"/><stop offset="1" stop-color="#d9dde6"/></radialGradient></defs>
  <circle cx="188" cy="188" r="176" fill="url(#girl)"/>
  <circle cx="188" cy="188" r="180" fill="none" stroke="var(--blue)" stroke-width="2.5"/>
  <circle cx="188" cy="188" r="186" fill="none" stroke="var(--navy)" stroke-width="2"/>
</svg>
<h2 class="script h2 abs" style="left:612px;top:1992px">Mein <b>Angebot</b> für Sie</h2>
<div class="text abs" style="left:612px;top:2058px;width:490px">
  <p>Lena (10) sitzt traurig im Sessel meiner Praxis und erzählt mir, dass sie Angst hat einzuschlafen. Sie sieht dunkle Gestalten mit riesengrossen Händen, die sie von unten packen wollen und ihr Vater muss jeden Abend bei ihr sitzen, bis sie eingeschlafen ist. Kurze Zeit später strahlt die Kleine und erzählt mir begeistert von Katzenbabys, Glitzer und bunten Spielsachen, die sie jetzt anstelle der dunklen Gestalten und Hände sieht.</p>
  <p>Zwei Wochen später sehe ich sie per Zufall auf dem Schulweg. Sie erzählt mir begeistert, dass sie kein einziges Mal mehr ihren Papa zum Einschlafen brauchte.</p>
  <p class="strong-blue">Solche Erfolge motivieren mich in meiner Coaching Tätigkeit. Schon nach zwei oder drei Sitzungen sind die Probleme einfach, schnell und leicht gelöst.</p>
</div>
<div class="text abs" style="left:200px;top:2440px;width:800px;text-align:center">
  <p>Ich coache Kinder und Erwachsene, die Ängste haben, die Probleme in der Schule haben und die ein Verhalten zeigen, welches sie nicht mehr haben wollen. Vom Nägelkauen, über Lernschwierigkeiten, bis zu Streit zu Hause oder Angst alleine in die Schule zu laufen oder ins Klassenlager zu fahren.</p>
  <p>Freuen Sie sich auf Frieden, Harmonie und Leichtigkeit zu Hause und in der Schule und kontaktieren Sie mich unverbindlich für ein Erstgespräch. Verbessern Sie Ihre Kommunikation mit Ihrem Kind.</p>
  <p>Im Einzelsetting wird als Erstes gemeinsam ein Ziel definiert, um Sie optimal zu unterstützen. Dieses wird im Laufe des Coachings immer wieder auf dessen Fortschritt geprüft.</p>
  <p>Eine meiner Stärken ist meine klare Kommunikation auf den Punkt, somit sind die Lösungen oftmals einfacher als anfangs vermutet. Indem ich Fragen stelle, die auch mal unangenehm und doch stets liebevoll und wertschätzend sind, finden wir rasch das für Sie passende Vorgehen.</p>
  <p>Beim Coachen von Kindern involviere ich immer auch die Eltern. Oftmals treffe ich zuerst nur die Eltern und die Kinder werden erst zu einem späteren Zeitpunkt involviert. Ich coache vor Ort oder per Videocall.</p>
</div>
<a class="btn abs" style="left:480px;top:2800px;width:247px" href="#">Zum Kontaktformular</a>

<!-- Testimonials -->
<h2 class="script h2 abs" style="left:110px;top:3090px">Was meine <b>Kunden</b> sagen</h2>
<div class="arrow abs" style="left:974px;top:3126px"><svg width="48" height="48" viewBox="0 0 48 48"><path d="M34 24H14M21 17L14 24L21 31" fill="none" stroke="#fff" stroke-width="2.4" stroke-linecap="round" stroke-linejoin="round"/></svg></div>
<div class="arrow abs" style="left:1036px;top:3126px"><svg width="48" height="48" viewBox="0 0 48 48"><path d="M14 24H34M27 17L34 24L27 31" fill="none" stroke="#fff" stroke-width="2.4" stroke-linecap="round" stroke-linejoin="round"/></svg></div>

<div class="card abs" style="left:110px;top:3253px;height:375px">
  <div class="q">“</div>
  <p>Sabine Merlinger ist ein wirklich sehr empathischer Coach! Sie hört total genau hin, gibt unglaublich passendes liebevolles Feedback und hat bei mir immer den Nagel genau auf den Kopf getroffen! Unglaublich, wieviel sich in schon so kurzer Zeit ändert – und das ganz leicht!</p>
  <div class="who"><div class="avatar" role="img" aria-label="Profilfoto der Kundin"></div><div><b>LAURA, 42</b><span class="stars">★★★★★</span></div></div>
</div>
<div class="card abs" style="left:445px;top:3283px;height:370px">
  <div class="q">“</div>
  <p>Sabine Merlinger ist ein wirklich sehr empathischer Coach! Sie hört total genau hin, gibt unglaublich passendes liebevolles Feedback und hat bei mir immer den Nagel genau auf den Kopf getroffen! Unglaublich, wieviel sich in schon so kurzer Zeit ändert – und das ganz leicht!</p>
  <div class="who"><div class="avatar" role="img" aria-label="Profilfoto der Kundin"></div><div><b>LAURA, 42</b><span class="stars">★★★★★</span></div></div>
</div>
<div class="card abs" style="left:778px;top:3218px;height:372px">
  <div class="q">“</div>
  <p>Sabine Merlinger ist ein wirklich sehr empathischer Coach! Sie hört total genau hin, gibt unglaublich passendes liebevolles Feedback und hat bei mir immer den Nagel genau auf den Kopf getroffen! Unglaublich, wieviel sich in schon so kurzer Zeit ändert – und das ganz leicht!</p>
  <div class="who"><div class="avatar" role="img" aria-label="Profilfoto der Kundin"></div><div><b>LAURA, 42</b><span class="stars">★★★★★</span></div></div>
</div>

<!-- Kontakt -->
<h2 class="script h2 abs" style="left:110px;top:3896px">Nehmen Sie <b>Kontakt</b><br>mit mir auf!</h2>
<p class="abs" style="left:110px;top:4016px;width:450px;line-height:21px">Gerne können Sie mich per Kontaktformular oder E-Mail für ein unverbindliches Erstgespräch kontaktieren, ich freue mich auf Sie!</p>
<div class="info abs" style="left:110px;top:4100px">
  <div class="ring"><svg width="22" height="26" viewBox="0 0 22 26"><path d="M11 25C11 25 2 15.5 2 9.5A9 9 0 0 1 20 9.5C20 15.5 11 25 11 25Z" fill="none" stroke="var(--navy)" stroke-width="1.6"/><circle cx="11" cy="9.5" r="3.2" fill="none" stroke="var(--navy)" stroke-width="1.6"/></svg></div>
  <div><b>Adresse</b>Lindenweg 12, CH-8600 Seefeld</div>
</div>
<div class="info abs" style="left:110px;top:4178px">
  <div class="ring"><svg width="26" height="20" viewBox="0 0 26 20"><rect x="1" y="1" width="22" height="15" rx="1.5" fill="none" stroke="var(--navy)" stroke-width="1.6"/><path d="M1.5 2L12 10L22.5 2" fill="none" stroke="var(--navy)" stroke-width="1.6"/></svg></div>
  <div><b>E-Mail</b>sabine@coach-merlinger.ch</div>
</div>

<div class="script abs" style="left:612px;top:4010px;font-size:28px;font-weight:400">Kontktformular</div>
<div class="field abs" style="left:612px;top:4062px;width:206px;height:46px">Name</div>
<div class="field abs" style="left:838px;top:4062px;width:206px;height:46px">E-Mail</div>
<div class="field abs" style="left:612px;top:4132px;width:432px;height:113px">Mitteilung</div>
<a class="btn abs" style="left:913px;top:4272px;width:131px" href="#">Abschicken</a>

<!-- Footer -->
<div class="footer abs" style="left:0;top:4433px;width:1200px;text-align:center">
  <a href="#">Impressum</a><a href="#">Datenschutz</a>
</div>

</body>
</html>
```